GPS business card

Brannery Works is the name of my company
GPS thats made to fit!

My Business is supply and install of IN DASH GPS SYSTEMS.
Small family based business that is mobile.

GPS touch screens that are built into the dash.
I have a logo I want Utilized
Wanting colours too

I have screens for all makes and models of vehicles.

I have attached a current business card and some photo's of the work I do.

Target Market(s)

new and used car buyers

Industry/Entity Type

Business

Requirements
Must have
• Name: Tom Brannery

Mob: 0438 215 604
email: tombrannery@mailvista.com

Must use logo

```html
<!DOCTYPE html>
<html lang="en">
<head>
<meta charset="utf-8">
<title>Brannery Works – Business Card</title>
<link rel="stylesheet" href="https://fonts.googleapis.com/css2?family=Arimo:wght@400;700&display=swap">
<style>
  :root {
    --card-black: #000000;
    --city-light: #5a5a5a;
    --city-mid: #2c2c2c;
    --city-dark: #121212;
    --brand-blue: #1b8bd3;
    --pin-blue: #1b87c9;
    --text-white: #ffffff;
  }
  * { margin: 0; padding: 0; box-sizing: border-box; }
  html, body {
    width: 1200px;
    height: 656px;
    overflow: hidden;
    background: var(--card-black);
  }
  .card {
    position: relative;
    width: 1200px;
    height: 656px;
    background: var(--card-black);
    font-family: "Arimo", Arial, sans-serif;
    color: var(--text-white);
    overflow: hidden;
  }
  .city-photo {
    position: absolute;
    left: 0;
    top: 0;
    width: 700px;
    height: 656px;
    background:
      linear-gradient(to right, rgba(0,0,0,0) 0%, rgba(0,0,0,0) 45%, rgba(0,0,0,0.7) 75%, var(--card-black) 100%),
      linear-gradient(to bottom, var(--city-dark) 0%, var(--city-light) 35%, var(--city-mid) 65%, var(--city-dark) 100%);
  }
  .location-pin {
    position: absolute;
    left: 0;
    top: 0;
    width: 520px;
    height: 560px;
  }
  .brand {
    position: absolute;
    right: 66px;
    top: 72px;
    display: flex;
    align-items: center;
    gap: 18px;
  }
  .brand-mark {
    width: 56px;
    height: 56px;
    background: var(--brand-blue);
  }
  .brand-name {
    font-weight: 700;
    font-size: 56px;
    line-height: 1;
    color: var(--brand-blue);
    white-space: nowrap;
  }
  .identity {
    position: absolute;
    right: 40px;
    top: 338px;
    text-align: right;
  }
  .person-name {
    font-weight: 700;
    font-size: 50px;
    line-height: 1;
    color: var(--brand-blue);
  }
  .person-role {
    margin-top: 10px;
    font-weight: 400;
    font-size: 35px;
    line-height: 1;
    color: var(--text-white);
  }
  .contact {
    position: absolute;
    right: 40px;
    top: 536px;
    text-align: right;
    font-size: 33px;
    line-height: 39px;
    font-weight: 400;
    color: var(--text-white);
  }
</style>
</head>
<body>
  <main class="card">
    <div class="city-photo" role="img" aria-label="Night-time photograph of a city skyline and a lit street seen from above"></div>

    <svg class="location-pin" viewBox="0 0 520 560" aria-hidden="true">
      <polygon points="198,388 320,388 264,508" fill="var(--pin-blue)"/>
      <circle cx="259" cy="278" r="115" fill="none" stroke="var(--pin-blue)" stroke-width="20"/>
    </svg>

    <header class="brand">
      <div class="brand-mark"></div>
      <div class="brand-name">Brannery Works</div>
    </header>

    <section class="identity">
      <h1 class="person-name">Tom Brannery</h1>
      <p class="person-role">Installation Technician</p>
    </section>

    <section class="contact">
      <p class="contact-phone">0438 215 604</p>
      <p class="contact-email">tombrannery@mailvista.com</p>
    </section>
  </main>
</body>
</html>
```